New Managed IT company needs a business card

We are an IT management and support company that needs a business card design. I have a logo that I'll provide. Blues and blacks match the logo, but i'm open to anything. I want the card to help people take us seriously, but still have some energy and fun in it. The card should communicate stability and a solid company.

Target Market(s)

Target market includes Owners and Presidents at small businesses of 20 - 100 employees in the Pittsburgh PA area.

Industry/Entity Type

Information Technology

Contact Information for Business Card

i am open to other designs, but i imagine having only the logo on one side and then the logo plus all contact details on the other side.

Requirements
Must have
• Our logo
• Company name is optional if the logo makes it obvious
• A name - Lew Tasker
• A title - President
• A phone number - 724-XXX-XXXX
• A mobile phone number - 724-516-0471
• An email address - ltasker@brightlanetech.com
• a website - brightlanetech.com or www.brightlanetech.com
Nice to have
• some people tell me the logo feels like a superhero theme, some fun with that idea might be good. I'm open to ideas.
Should not have
• stock photos of people or computers - especially old looking stuff.

```html
<!DOCTYPE html>
<html lang="en">
<head>
<meta charset="utf-8">
<title>Brightlane Tech — Business Card</title>
<link href="https://fonts.googleapis.com/css2?family=Montserrat:wght@400;500;700&display=swap" rel="stylesheet">
<style>
  :root {
    --page: #e9e6e1;
    --card-white: #fbfbfb;
    --card-black: #0b0b0c;
    --ink-dark: #3a3a3c;
    --ink-mid: #5d5d60;
    --accent-blue: #29a8df;
    --rule: #4a4a4c;
    --faint: #e1e1e2;
    --brand-light: #d9dadc;
  }
  * { box-sizing: border-box; margin: 0; padding: 0; }
  html, body {
    width: 771px; height: 1200px; overflow: hidden;
    background: var(--page);
    font-family: "Montserrat", sans-serif;
  }
  .canvas {
    position: relative; width: 771px; height: 1200px;
  }
  .card {
    position: absolute; left: 76px; width: 620px; height: 354px;
    overflow: hidden;
    box-shadow: 0 6px 18px rgba(0,0,0,0.18);
  }

  /* Front: contact side */
  .card-front { top: 170px; background: var(--card-white); }
  .corner-rule {
    position: absolute; left: 40px; top: 0; width: 150px; height: 78px;
    border-right: 1.5px solid var(--rule);
    border-bottom: 1.5px solid var(--rule);
  }
  .identity { position: absolute; left: 54px; top: 112px; z-index: 2; }
  .person-name {
    font-weight: 700; font-size: 22px; letter-spacing: 3px;
    color: var(--ink-dark); text-transform: uppercase;
  }
  .person-title {
    margin-top: 4px;
    font-weight: 700; font-size: 12px; letter-spacing: 2.5px;
    color: var(--accent-blue); text-transform: uppercase;
  }
  .contact-list { list-style: none; margin-top: 22px; }
  .contact-item {
    display: flex; align-items: center; gap: 12px;
    font-size: 13.5px; color: var(--ink-mid); line-height: 26px;
  }
  .contact-icon { width: 15px; height: 15px; flex: none; }
  .brand-faint {
    position: absolute; right: 34px; bottom: 24px; z-index: 1;
    display: flex; align-items: center; gap: 12px;
  }
  .brand-faint .brand-dot {
    width: 36px; height: 36px; border-radius: 50%;
    background: var(--faint);
  }
  .brand-faint .brand-name {
    font-weight: 700; font-size: 24px; letter-spacing: 2px;
    color: var(--faint); text-transform: uppercase; line-height: 1;
  }

  /* Back: brand side */
  .card-back {
    top: 690px;
    background: radial-gradient(ellipse at 50% 50%, #2a2d31 0%, #141516 45%, var(--card-black) 80%);
  }
  .brand-lockup {
    position: absolute; left: 0; right: 0; top: 0; bottom: 0;
    display: flex; align-items: center; justify-content: center; gap: 18px;
  }
  .brand-lockup .brand-dot {
    width: 62px; height: 62px; border-radius: 50%;
    background: var(--accent-blue);
  }
  .brand-lockup .brand-name {
    font-weight: 700; font-size: 36px; letter-spacing: 3px;
    color: var(--brand-light); text-transform: uppercase;
  }
</style>
</head>
<body>
<main class="canvas">

  <section class="card card-front" aria-label="Business card, contact side">
    <div class="corner-rule"></div>

    <div class="brand-faint" aria-hidden="true">
      <span class="brand-dot"></span>
      <span class="brand-name">Brightlane Tech</span>
    </div>

    <div class="identity">
      <h1 class="person-name">Lew Tasker</h1>
      <p class="person-title">President</p>

      <ul class="contact-list">
        <li class="contact-item">
          <svg class="contact-icon" viewBox="0 0 16 16" aria-hidden="true">
            <rect x="1" y="2" width="14" height="12" rx="2" fill="var(--accent-blue)"/>
            <path d="M4.5 5.5c0 3 2.5 5.5 5.5 5.5l1-1.4-1.6-1-0.8.8c-1-.4-1.8-1.2-2.2-2.2l.8-.8-1-1.6z" fill="#fff"/>
          </svg>
          <span>724-XXX-XXXX</span>
        </li>
        <li class="contact-item">
          <svg class="contact-icon" viewBox="0 0 16 16" aria-hidden="true">
            <rect x="4" y="1" width="8" height="14" rx="1.5" fill="none" stroke="var(--accent-blue)" stroke-width="1.5"/>
            <circle cx="8" cy="12.3" r="0.9" fill="var(--accent-blue)"/>
          </svg>
          <span>724-516-0471</span>
        </li>
        <li class="contact-item">
          <svg class="contact-icon" viewBox="0 0 16 16" aria-hidden="true">
            <rect x="1" y="3" width="14" height="10" rx="1" fill="var(--accent-blue)"/>
            <path d="M1.5 3.8 8 9l6.5-5.2" fill="none" stroke="#fff" stroke-width="1.2"/>
          </svg>
          <span>ltasker@brightlanetech.com</span>
        </li>
        <li class="contact-item">
          <svg class="contact-icon" viewBox="0 0 16 16" aria-hidden="true">
            <circle cx="8" cy="8" r="6.8" fill="none" stroke="var(--accent-blue)" stroke-width="1.3"/>
            <ellipse cx="8" cy="8" rx="3" ry="6.8" fill="none" stroke="var(--accent-blue)" stroke-width="1.1"/>
            <path d="M1.4 8h13.2M2.5 4.6h11M2.5 11.4h11" stroke="var(--accent-blue)" stroke-width="1.1"/>
          </svg>
          <span>www.brightlanetech.com</span>
        </li>
      </ul>
    </div>
  </section>

  <section class="card card-back" aria-label="Business card, brand side">
    <div class="brand-lockup">
      <span class="brand-dot"></span>
      <span class="brand-name">Brightlane Tech</span>
    </div>
  </section>

</main>
</body>
</html>
```